Thank You Card from Pediatric Dentist to Pediatrician - April Showers Promo

We are doing a promo where we are giving local pediatricians and their staff members personalized umbrellas as a thank you for continued referrals of pediatric dental patients. "April Shower Bring May Flowers" Promo. The card will be printed and tied around the umbrella with ribbon... Can be 5x7 or 4x8. Needs to include text and logos below.

Target Market(s)

Pediatricians and their staff members - fun, bright colors

Industry/Entity Type

Medical

Font styles to use
Other font styles liked:
• something fun and bold

Colors
85cae6

Requirements
Must have
• 5x7 or 4x8 single sided card
• must included toothglimmer logo, some umbrella image, and "April Showers Bring May Flowers".
• Needs to include the following text:
• "We are grateful for your continued trust this year. We thank you and wish you and your loved ones a fun-filled summer! Together, we strive to promote the highest level of oral and systemic health for "our kids"!
• Mark Tellwin DMD, Derek Tellwin DMD, Monica Tellwin DMD, Wendy Tellwin COO, Colleen Tellwin DMD, Ruth Tellwin DMD, Associates and Staff"
Nice to have
• see attached copy of our last design crown project
• if room:
• Philadelphia's Premier Pediatric Dental Practice for over 35 Years!

```html
<!DOCTYPE html>
<html lang="en">
<head>
<meta charset="utf-8">
<title>April Showers Thank You Card</title>
<link rel="stylesheet" href="https://fonts.googleapis.com/css2?family=Parisienne&family=Roboto:wght@300;400;700&family=Roboto+Condensed:wght@700&display=swap">
<style>
  :root {
    --cream: #f6efe0;
    --cream-deep: #efe4cf;
    --card: #ffffff;
    --script-red: #e0262b;
    --band-red: #d8262a;
    --ink: #2e2e2e;
    --navy: #1c2a5b;
    --teal: #2e6b80;
    --coral: #ef7a5c;
    --sun: #f4d35e;
    --leaf: #a9cc6b;
  }
  * { margin: 0; padding: 0; box-sizing: border-box; }
  html, body { width: 857px; height: 1200px; overflow: hidden; }
  body { position: relative; font-family: "Roboto", Arial, sans-serif; background: var(--cream); }

  .umbrella-pattern {
    position: absolute; inset: 0;
    background:
      radial-gradient(ellipse 260px 160px at 12% 10%, rgba(239,122,92,0.35), transparent 70%),
      radial-gradient(ellipse 260px 160px at 30% 4%, rgba(46,107,128,0.35), transparent 70%),
      radial-gradient(ellipse 260px 160px at 72% 6%, rgba(169,204,107,0.4), transparent 70%),
      radial-gradient(ellipse 240px 160px at 96% 14%, rgba(46,107,128,0.35), transparent 70%),
      radial-gradient(ellipse 220px 180px at 2% 52%, rgba(46,107,128,0.3), transparent 70%),
      radial-gradient(ellipse 220px 180px at 98% 52%, rgba(46,107,128,0.3), transparent 70%),
      radial-gradient(ellipse 220px 160px at 4% 70%, rgba(169,204,107,0.35), transparent 70%),
      radial-gradient(ellipse 220px 160px at 96% 72%, rgba(169,204,107,0.35), transparent 70%),
      radial-gradient(ellipse 260px 160px at 14% 94%, rgba(244,211,94,0.4), transparent 70%),
      radial-gradient(ellipse 260px 160px at 50% 94%, rgba(169,204,107,0.4), transparent 70%),
      radial-gradient(ellipse 260px 160px at 86% 94%, rgba(239,122,92,0.35), transparent 70%),
      linear-gradient(160deg, var(--cream) 0%, var(--cream-deep) 100%);
  }

  .thank-you-card {
    position: absolute; left: 118px; top: 205px; width: 621px; height: 788px;
    background: var(--card);
    box-shadow: 0 6px 18px rgba(0,0,0,0.28);
  }

  .floral-umbrella {
    position: absolute; left: 60px; top: 28px; width: 140px; height: 84px;
    border-radius: 70px 70px 8px 8px;
    background: linear-gradient(180deg, var(--coral) 0%, var(--sun) 40%, var(--leaf) 70%, var(--teal) 100%);
    opacity: 0.85;
  }

  .headline {
    position: absolute; left: 0; top: 0; width: 621px; height: 200px;
    font-family: "Parisienne", cursive; font-weight: 400;
    color: var(--script-red);
    font-size: 52px; line-height: 60px; white-space: nowrap;
  }
  .headline .line-one { position: absolute; left: 214px; top: 40px; }
  .headline .line-two { position: absolute; left: 162px; top: 108px; }

  .message {
    position: absolute; left: 95px; top: 218px; width: 431px;
    text-align: center; color: var(--ink);
    font-weight: 400; font-size: 22px; line-height: 32.6px;
  }

  .practice-mark {
    position: absolute; left: 62px; top: 455px; width: 190px; height: 190px;
    display: flex; flex-direction: column; align-items: center; justify-content: center; gap: 12px;
  }
  .practice-mark .mark-dot {
    width: 70px; height: 70px; border-radius: 50%; background: var(--teal);
  }
  .practice-mark .mark-name {
    font-weight: 700; font-size: 22px; line-height: 26px; color: var(--navy); text-align: center;
  }

  .team-list {
    position: absolute; left: 284px; top: 446px; list-style: none;
  }
  .team-list li {
    position: relative; padding-left: 15px; white-space: nowrap;
    font-weight: 700; font-size: 23px; line-height: 30.2px; color: var(--navy);
  }
  .team-list li::before {
    content: ""; position: absolute; left: 0; top: 12px;
    width: 8px; height: 8px; border-radius: 50%; background: var(--navy);
  }

  .legacy-band {
    position: absolute; left: 0; top: 692px; width: 621px; height: 28px;
    background: var(--band-red);
    color: #fff; text-align: center; white-space: nowrap;
    font-family: "Roboto Condensed", "Arial Narrow", sans-serif;
    font-weight: 700; font-size: 16px; line-height: 28px;
  }

  .website {
    position: absolute; left: 0; top: 736px; width: 621px; text-align: center;
    font-weight: 700; font-size: 19px; color: var(--navy);
  }
</style>
</head>
<body>
  <div class="umbrella-pattern" role="img" aria-label="Repeating pattern of polka-dot umbrellas in teal, coral, yellow and green on a cream background"></div>

  <section class="thank-you-card">
    <div class="floral-umbrella" role="img" aria-label="Umbrella made of colourful leaves and flowers with raindrops falling beneath"></div>

    <h1 class="headline">
      <span class="line-one">April Showers</span>
      <span class="line-two">Bring May Flowers</span>
    </h1>

    <p class="message">We are grateful for your continued trust this year. We thank you and wish you and your loved ones a fun-filled summer! Together, we strive to promote the highest level of oral and systemic health for "our kids"!</p>

    <div class="practice-mark">
      <span class="mark-dot"></span>
      <span class="mark-name">Doc Tellwin's<br>Tooth Glimmer</span>
    </div>

    <ul class="team-list">
      <li>Mark Tellwin DMD</li>
      <li>Derek Tellwin DMD</li>
      <li>Monica Tellwin DMD</li>
      <li>Wendy Tellwin COO</li>
      <li>Colleen Tellwin DMD</li>
      <li>Ruth Tellwin DMD</li>
      <li>Associates and Staff</li>
    </ul>

    <div class="legacy-band">Philadelphia's Premier Pediatric Dental Practice for over 35 Years!</div>

    <div class="website">www.toothglimmers.com</div>
  </section>
</body>
</html>
```